Wordpress Template for Biomed tech startup

Needed: A wordpress based site ready to go with custom logo and icons - all we would have to do is add text and pics
We are a Princeton based startup company. We are currently developing advanced prosthetics that will be commercial in the next few years - in the meantime, we would like to sell robotics kits to get students and adults interested in Science, Tech, Math, and Engineering.

Our company is called Quellrion.

Our first few kits include:
- A Robotic Arm kit (DIY kit allows you to build a robotic hand that has 8 points of movement)
- Sensor Glove Kit (use in conjunction with the robotic hand to have it mimic the actions your hand does with the glove on - or use it for other tech applications)

Target Market(s)

Makers, DIY community, students, science oriented young adults, investors

Industry/Entity Type

It Company

Requirements
Must have
• -Ecommerce ability (a plugin like Tobrix would suffice)

Detailed creative brief Below:

Background

There is no current website for Quellrion. In order to drive the progression of the company, there must be a website that will provide potential customers, investors, and employees with information about the company and how it came to be. The website must allow for users to discover information about the company, the products that are made and how to go about purchasing products. We want the website to be sleek and simple to appeal to our audience of technology oriented “makers”.

Communications Objectives
The objectives of this website are:

Provide information about the products that Quellrion has developed.
Provide an avenue for potential customers to connect with Quellrion
Display why our products are great for makers and other people interested in robotic-type products.

Tactical Objectives
EXTERNAL: The tactical objective is to create an inviting tool to help past, present, and future customers understand our business and validate their decision in purchasing our products.

INTERNAL: Establish a compelling site that is attracting potential customers. The website will also be a tool I helping to attract potential employees to the company.

Target Audience
“Makers” who would be interested in purchasing our products and/or who would discuss our product with friends, co-workers, etc. who have similar interests. Potential future employees could also discover us through the website. Investors.

Tone and Manner
Innovative, Technological, Approachable, Fresh

Mandatories
Must include Quellrion logo
Focal colors - Keep logo in mind

Mapping and Layout

Home Page:
• MANDATORIES:
• Quellrion logo
• Slideshow with 5 pictures
• Facebook
• Twitter
• Video from YouTube or Vimeo

About Us

Founder backstory
History of how founder began his work and why
Story of Quellrion Creation
How the company came to be and what it took to start it

Investors Page -Password protected "investors" page - if a potential investor doesnt have a password to this page they may fill out an e-form with their information (which should be emailed to a Quellrion employee for approval) and they get the password to access after approval.

Prosthetic Hand

Info about the hand
Video of the hand working

Robotic Hand Kits

Info about the hand kit
Video/commercial of the hand
Option to purchase the kit

Glove Kits

Info about the hand kit

Contact Us

Contact information page for visitors to fill out a contact us form
Our Contact info as well

Nice to have
• Background and text similar to that of business card

```html
<!DOCTYPE html>
<html lang="en">
<head>
<meta charset="utf-8">
<title>Quellrion — Robotics Kits &amp; Prosthetics</title>
<link href="https://fonts.googleapis.com/css2?family=Source+Sans+3:wght@400;600&family=Oswald:wght@500&display=swap" rel="stylesheet">
<style>
:root{
  --blue:#2b5ea6;
  --blue-logo:#3a6cb4;
  --ink:#333;
  --muted:#666;
  --line:#dcdcdc;
  --panel:#f4f4f4;
  --footer:#f0f0f0;
  --dark:#1b1b1b;
  --top:#444;
}
*{box-sizing:border-box;margin:0;padding:0}
html,body{width:849px;height:1200px;overflow:hidden;background:#fff}
body{position:relative;font-family:"Source Sans 3",Arial,sans-serif;color:var(--ink)}
.abs{position:absolute}
.topbar{left:0;top:0;width:849px;height:8px;background:var(--top)}
.logo{left:60px;top:8px;width:149px;height:111px;background:var(--blue-logo);
  clip-path:polygon(0 0,100% 0,100% 100%,50% 87%,0 100%);
  display:flex;align-items:center;justify-content:center;padding-bottom:26px}
.logo span{color:#fff;font-size:21px;font-weight:400;letter-spacing:-.2px}
.utility{right:61px;top:31px;display:flex;font-size:11px;color:#444}
.utility a{color:inherit;text-decoration:none;padding:0 13px;border-left:1px dotted #bbb}
.utility a:first-child{border-left:none}
.utility a:last-child{padding-right:0}
.cart{left:509px;top:76px;font-size:11px;color:#444;display:flex;align-items:center;gap:5px}
.search{left:627px;top:71px;width:161px;height:25px;border:1px solid #ccc;border-radius:2px;
  font-size:9px;font-style:italic;color:#aaa;padding:6px 0 0 5px}
.search svg{position:absolute;right:6px;top:6px}
.mainnav{left:60px;top:138px;width:729px;height:46px;background:var(--panel);border:1px solid #e2e2e2;
  border-bottom:4px solid var(--blue);display:flex;align-items:center;padding-left:5px}
.mainnav a{font-size:11.8px;color:#333;text-decoration:none;padding:0 17px;border-left:1px dotted #bbb;line-height:14px}
.mainnav a:first-child{border-left:none;padding-left:11px}
.hero{left:60px;top:184px;width:729px;height:316px;
  background:linear-gradient(110deg,#2b2a28 0%,#6c6862 30%,#8a857c 48%,#3d3a35 72%,#141311 100%)}
.caption{left:78px;top:376px;width:333px;height:124px;background:rgba(40,40,40,.72);padding:10px 16px}
.caption h2{font-family:Oswald,Impact,sans-serif;font-weight:500;font-size:23px;color:#fff;letter-spacing:.3px;line-height:26px}
.caption h3{font-weight:400;font-size:15.5px;color:#fff;margin-top:5px;line-height:18px}
.caption p{font-size:11px;color:#f2f2f2;line-height:17.5px;margin-top:6px}
.dots{left:733px;top:483px;display:flex;gap:3px}
.dots i{width:9px;height:9px;border-radius:50%;background:#fff}
.dots i:first-child{background:#888}
.feature{top:527px;height:67px;background:var(--panel);border:1px solid #e0e0e0;display:flex;align-items:center}
.feature .icon{width:66px;display:flex;justify-content:center}
.feature h4{font-size:15px;font-weight:400;color:var(--blue);line-height:17px}
.feature small{display:block;font-size:9.5px;color:#555;margin-top:6px}
.heading{font-size:14px;color:var(--blue);font-weight:400}
.card{top:643px;height:128px;border:1px solid #e5e5e5;background:#fff}
.card .thumb{position:absolute;left:8px;top:20px;width:94px;height:72px;border-radius:3px}
.card .name{position:absolute;left:112px;top:17px;width:112px;font-size:11.3px;color:var(--blue);line-height:18px}
.card .price{position:absolute;left:115px;top:60px;font-size:11px;color:#444}
.card .btn{position:absolute;left:118px;top:91px;background:#1e1e1e;color:#fff;font-size:9.3px;padding:4px 6px;border:1px solid #555;border-radius:2px}
.video{left:60px;top:831px;width:253px;height:132px;background:linear-gradient(90deg,#0d0d0d 0%,#1f1f1f 40%,#3b3128 60%,#0f0f0f 100%)}
.video svg{position:absolute;left:103px;top:48px}
.copy{left:335px;top:828px;width:456px;font-size:9.1px;color:#666;line-height:15.3px}
.copy p+p{margin-top:2px}
.footer{left:0;top:997px;width:849px;height:147px;background:var(--footer)}
.fcol{top:1010px}
.fcol h5{font-size:11.2px;font-weight:400;color:#333;margin-bottom:5px}
.fcol li{list-style:none;font-size:9.6px;color:#444;line-height:20.4px}
.newsletter{left:645px;top:1045px;width:144px;height:24px;background:#cfcfcf;border-radius:2px}
.newsletter span{position:absolute;right:5px;top:2px;color:#fff;font-size:15px}
.social{left:645px;top:1089px;display:flex;gap:-2px}
.social i{width:21px;height:21px;border-radius:50%;background:#8d8d8d;border:1px solid #fff;margin-right:-1px}
.bottombar{left:0;top:1144px;width:849px;height:56px;background:var(--dark)}
.bottombar p{position:absolute;left:63px;top:23px;font-size:9.5px;color:#ddd}
</style>
</head>
<body>
<div class="abs topbar"></div>

<header>
  <div class="abs logo"><span>Quellrion</span></div>
  <nav class="abs utility">
    <a href="#">HOME</a><a href="#">WISH LIST (0)</a><a href="#">MY ACCOUNT</a><a href="#">CHECK OUT</a><a href="#">LOGIN</a><a href="#">CREATE AN ACCOUNT</a>
  </nav>
  <div class="abs cart">
    <svg width="14" height="12" viewBox="0 0 14 12"><path d="M0 1h3l2 7h7l1.5-5H4" fill="none" stroke="#c33" stroke-width="1.3"/><circle cx="6" cy="10.5" r="1.2" fill="#555"/><circle cx="11" cy="10.5" r="1.2" fill="#555"/></svg>
    Cart (0) items
  </div>
  <div class="abs search">Search..
    <svg width="11" height="11" viewBox="0 0 11 11"><circle cx="4.5" cy="4.5" r="3.4" fill="none" stroke="#888" stroke-width="1.5"/><path d="M7 7l3 3" stroke="#888" stroke-width="1.7"/></svg>
  </div>
  <nav class="abs mainnav">
    <a href="#">HOME</a><a href="#">ABOUT US</a><a href="#">INVESTORS PAGE</a><a href="#">PROSTHETIC HAND</a><a href="#">ROBOTIC HAND KITS</a><a href="#">GLOVE KITS</a><a href="#">CONTACT US</a>
  </nav>
</header>

<section>
  <div class="abs hero" role="img" aria-label="Photo of a white robotic hand with tendon wires mounted on a metal servo assembly"></div>
  <div class="abs caption">
    <h2>SELLENTESQUE CURSUS</h2>
    <h3>DIGNISSIM PHARETRA ERO</h3>
    <p>Jerta baditaut onsequser untur magni dolores eoquie volup tate msequi nesciunt. Voluptatem accusantium dolorem.</p>
  </div>
  <div class="abs dots"><i></i><i></i><i></i><i></i></div>
</section>

<section>
  <div class="abs feature" style="left:61px;width:238px">
    <div class="icon"><svg width="42" height="34" viewBox="0 0 42 34"><path d="M2 4h24v20H2z" fill="#6d8fc2"/><path d="M27 11h8l6 7v6H27z" fill="#6d8fc2"/><circle cx="9" cy="27" r="4.5" fill="#6d8fc2" stroke="#f4f4f4" stroke-width="2"/><circle cx="33" cy="27" r="4.5" fill="#6d8fc2" stroke="#f4f4f4" stroke-width="2"/></svg></div>
    <div><h4>FREE SHIPPING</h4><small>THIS OFFER IS VALID ON ALL STORES</small></div>
  </div>
  <div class="abs feature" style="left:305px;width:237px">
    <div class="icon"><svg width="38" height="38" viewBox="0 0 38 38"><path d="M6 3l7 0 3 9-5 4c3 6 6 9 12 12l4-5 9 3v7c-1 2-3 3-6 3C16 34 4 22 3 9c0-3 1-5 3-6z" fill="#6d8fc2"/></svg></div>
    <div><h4>CALL +1 (555) 010 0199</h4><small>OUR EXPERIENCED AND HIGHLY</small></div>
  </div>
  <div class="abs feature" style="left:549px;width:239px">
    <div class="icon"><svg width="38" height="38" viewBox="0 0 38 38"><circle cx="19" cy="19" r="18" fill="#6d8fc2"/></svg></div>
    <div><h4>OUR BLOG</h4><small>GET CONNECTED TO OUR BLOG</small></div>
  </div>
</section>

<section>
  <h3 class="abs heading" style="left:61px;top:616px">LATEST PRODUCTS</h3>
  <div class="abs card" style="left:62px;width:229px">
    <div class="thumb" role="img" aria-label="Product photo of a yellow and black robotic arm kit" style="background:linear-gradient(135deg,#fff 10%,#d9c36b 45%,#333 70%,#fff 95%)"></div>
    <div class="name">Kelvaro Flexion Servo Arm Kit</div>
    <div class="price">Price : $146.00 (-3%)</div>
    <div class="btn">MORE DETAILS</div>
  </div>
  <div class="abs card" style="left:308px;width:229px">
    <div class="thumb" role="img" aria-label="Product photo of a pair of black sensor gloves" style="background:linear-gradient(90deg,#fff 8%,#2a2a2a 30%,#fff 50%,#2a2a2a 70%,#fff 92%)"></div>
    <div class="name">Kelvaro Flexion Servo Arm Kit</div>
    <div class="price">Price : $146.00 (-3%)</div>
    <div class="btn">MORE DETAILS</div>
  </div>
  <div class="abs card" style="left:558px;width:230px">
    <div class="thumb" role="img" aria-label="Product photo of a black robotic arm on a stand" style="background:linear-gradient(40deg,#fff 15%,#2d3338 45%,#fff 85%)"></div>
    <div class="name">Kelvaro Flexion Servo Arm Kit</div>
    <div class="price">Price : $146.00 (-3%)</div>
    <div class="btn">MORE DETAILS</div>
  </div>
</section>

<section>
  <h3 class="abs heading" style="left:60px;top:799px">HOW IT WORKS?</h3>
  <div class="abs video" role="img" aria-label="Video still of a person holding a gold and silver prosthetic hand">
    <svg width="38" height="38" viewBox="0 0 38 38"><circle cx="19" cy="19" r="17" fill="rgba(0,0,0,.55)" stroke="#fff" stroke-width="2.5"/><path d="M14 11l13 8-13 8z" fill="#fff"/></svg>
  </div>
  <div class="abs copy">
    <p>Have a Brenzio product and it iyou can't wait to get your' hands on! We leverage the intuitive features and touchscreen technology found in the Orbix family of products to make your tools easier to use than ever. As first-to-market in Orbix Test, we have established ourselves as leaders in this new category. Update your test equipment platform to the Orbix Phone, Orbix Tab or Orbix Play and select from a variety of innovative products, including:</p>
    <p>Envie uma foto de seu prato para nossa avaliação. Desta forma, podemos lhe conceder dicas de como tornar a sua refeição mais nutritiva e saudável. Se alimentar die forma correta tem se tornado motivo de estresse para algumas pessoas atualmente. Hoje em dia, com Envie uma foto de seu prato para nossa avaliação. Desta forma, podemos lhe conceder dicas de como tornar a sua refeição mais nutritiva e saudável. Conheça todos os serviços que a Verdola oferece para você e/ou sua empresa.</p>
  </div>
</section>

<footer>
  <div class="abs footer"></div>
  <div class="abs fcol" style="left:65px"><h5>Customer Services</h5><ul><li>Shopping Guide</li><li>Contact Us</li><li>FAQ</li><li>Track My Order</li><li>Return Policy</li></ul></div>
  <div class="abs fcol" style="left:220px"><h5>My Account</h5><ul><li>Sign in | Register</li><li>Order History</li><li>Messages</li><li>Points &amp; Coupons, Gifts</li><li>RMA Request</li></ul></div>
  <div class="abs fcol" style="left:372px"><h5>Company Info</h5><ul><li>Legal window</li><li>About Us</li><li>Why Buy From Us</li><li>Security &amp; Privacy</li><li>Terms of Use</li></ul></div>
  <div class="abs fcol" style="left:509px"><h5>Partner Program</h5><ul><li>Wholesale</li><li>Affiliate Program</li><li>Partner links</li><li>Drop-shipping</li></ul></div>
  <div class="abs fcol" style="left:645px"><h5>Newsletter</h5></div>
  <div class="abs newsletter"><span>»</span></div>
  <div class="abs social"><i></i><i></i><i></i><i></i></div>
  <div class="abs bottombar"><p>© 2013 Copyrights Reserved. All rights reserved.</p></div>
</footer>
</body>
</html>
```